Harbor Business Cards

I need a business card designed with the following information.

Company Name: Harbor Wealth Management
Name: BriAnne Dockery
Title: Executive Assistant
Cell: (541) 555-0173
Direct Line: (458) 555-0148
Email: brianne@harborwmx.com
Address: 20537 W. Marlowe PKWY Ste. B
Carver Bay, OR 97390

I have attached the logo.
I would like it in navy blue and silver.
Thanks.

```html
<!DOCTYPE html>
<html lang="en">
<head>
<meta charset="utf-8">
<title>Harbor Wealth Management – Business Card</title>
<link rel="stylesheet" href="https://fonts.googleapis.com/css2?family=Marcellus&display=swap">
<style>
  :root {
    --navy: #0d2240;
    --silver: #e9ecf0;
    --white: #ffffff;
    --paper: #f7f7f7;
    --backdrop: #d8d4cd;
  }
  * { margin: 0; padding: 0; box-sizing: border-box; }
  html, body { width: 900px; height: 1200px; overflow: hidden; }
  body {
    background: var(--backdrop);
    font-family: "Marcellus", "Optima", serif;
    position: relative;
  }
  .card {
    position: absolute;
    left: 80px;
    width: 732px;
    height: 428px;
    border-radius: 28px;
  }
  .card-front { top: 130px; background: var(--navy); color: var(--white); }
  .card-back { top: 645px; background: var(--paper); color: var(--navy); }

  .mark {
    position: absolute;
    border-radius: 50%;
  }
  .card-front .mark {
    left: 67px; top: 135px;
    width: 160px; height: 160px;
    background: var(--white);
  }
  .divider {
    position: absolute;
    left: 282px; top: 98px;
    width: 1.5px; height: 240px;
    background: var(--silver);
  }
  .details {
    position: absolute;
    left: 322px; top: 92px;
  }
  .brand-name {
    font-size: 38px;
    letter-spacing: 13px;
    line-height: 1;
    white-space: nowrap;
  }
  .brand-tagline {
    font-size: 15px;
    letter-spacing: 3.4px;
    line-height: 1;
    white-space: nowrap;
  }
  .card-front .brand-tagline { margin: 12px 0 0 24px; }
  .person-name {
    margin-top: 25px;
    font-size: 24px;
    letter-spacing: 1.5px;
    line-height: 1;
  }
  .person-title {
    margin-top: 5px;
    font-size: 15px;
    letter-spacing: 0.8px;
    color: var(--silver);
  }
  .contact {
    list-style: none;
    margin-top: 14px;
    font-size: 14.5px;
    color: var(--silver);
  }
  .contact li { line-height: 26px; white-space: nowrap; }

  .card-back .mark {
    left: 301px; top: 103px;
    width: 130px; height: 130px;
    background: var(--navy);
  }
  .back-brand {
    position: absolute;
    left: 0; right: 0; top: 264px;
    text-align: center;
  }
  .back-brand .brand-name { padding-left: 13px; }
  .back-brand .brand-tagline { margin-top: 10px; padding-left: 3px; }
</style>
</head>
<body>
  <section class="card card-front">
    <div class="mark"></div>
    <div class="divider"></div>
    <div class="details">
      <div class="brand-name">HARBOR</div>
      <div class="brand-tagline">WEALTH MANAGEMENT</div>
      <div class="person-name">BRIANNE DOCKERY</div>
      <div class="person-title">EXECUTIVE ASSISTANT</div>
      <ul class="contact">
        <li>M: (541) 555-0173</li>
        <li>P: (458) 555-0148</li>
        <li>E: brianne@harborwmx.com</li>
        <li>A: 20537 W. Marlowe PKWY Ste. B, Carver Bay, OR 97390</li>
      </ul>
    </div>
  </section>

  <section class="card card-back">
    <div class="mark"></div>
    <div class="back-brand">
      <div class="brand-name">HARBOR</div>
      <div class="brand-tagline">WEALTH MANAGEMENT</div>
    </div>
  </section>
</body>
</html>
```